Night Dresses business cards business requirers

We are a new company initiating Mexico operations. Our core business is Night woman dress (both formal and party dress) for rent. Gownhaven is the name of the company. ITS Gownhaven form by two word. The dress word and topia (Utopic) so the place Gownhaven Means That You cant get the ideal, perfect and unique dress for your event. So we would like a modern, very creative, and attractive business card.

Industry/Entity Type

Womens Clothing

Contact Information for Business Card

Rounded Borders, two faces

Requirements
Must have
• Rounded borders, logo and slogan, modern, glam, attractive design
Should not have
• modern design classic or not

```html
<!DOCTYPE html>
<html lang="en">
<head>
<meta charset="utf-8">
<title>Gownhaven business cards</title>
<link rel="stylesheet" href="https://fonts.googleapis.com/css2?family=Josefin+Sans:wght@400;600&family=Oswald:wght@400&display=swap">
<style>
  :root {
    --backdrop: #f2d3dd;
    --silk-light: #e08ab0;
    --silk-mid: #c9588c;
    --silk-dark: #a23e6c;
    --satin-white: #f7f4f2;
    --satin-shade: #e6e1de;
    --gold-light: #f6d64a;
    --gold-mid: #d9a916;
    --gold-dark: #b07f08;
    --ink: #2b2326;
    --plum: #a8457a;
  }
  * { box-sizing: border-box; margin: 0; padding: 0; }
  html, body {
    width: 1200px; height: 856px; overflow: hidden;
    background: var(--backdrop);
    font-family: "Josefin Sans", sans-serif;
    color: var(--ink);
  }
  .sheet {
    width: 1200px; height: 856px;
    display: flex; flex-direction: column; align-items: center; justify-content: center;
    gap: 44px;
  }
  .card {
    position: relative;
    width: 620px; height: 354px;
    border-radius: 28px;
    overflow: hidden;
    box-shadow: 0 10px 26px rgba(140, 50, 90, 0.22);
  }
  .silk {
    position: absolute; inset: 0;
    background:
      linear-gradient(120deg, transparent 20%, rgba(255,255,255,0.18) 32%, transparent 44%, rgba(0,0,0,0.08) 60%, transparent 72%),
      linear-gradient(160deg, var(--silk-light), var(--silk-mid) 45%, var(--silk-dark));
  }
  .gold {
    background: linear-gradient(100deg, var(--gold-dark), var(--gold-light) 25%, var(--gold-mid) 50%, var(--gold-light) 75%, var(--gold-dark));
  }
  .satin {
    background: linear-gradient(135deg, var(--satin-white), var(--satin-shade) 40%, var(--satin-white) 70%, var(--satin-shade));
  }

  /* Brand wordmark: name with a plain square beside it */
  .wordmark {
    display: flex; align-items: center; gap: 8px;
    font-weight: 400; letter-spacing: 0.2em; color: var(--ink);
  }
  .wordmark-square {
    flex: none; background: var(--plum);
  }
  .slogan {
    font-weight: 400; letter-spacing: 0.18em; color: var(--ink);
  }

  /* Front face */
  .front-frame {
    position: absolute; left: 50%; top: 50%;
    width: 244px; height: 244px;
    transform: translate(-50%, -50%);
    padding: 20px;
  }
  .front-panel {
    width: 100%; height: 100%;
    padding: 7px;
  }
  .front-inset {
    width: 100%; height: 100%;
    border: 2px solid var(--ink);
    display: flex; flex-direction: column; align-items: center; justify-content: center;
    gap: 12px;
  }
  .front-inset .wordmark { font-size: 16px; }
  .front-inset .wordmark-square { width: 10px; height: 10px; }
  .front-inset .slogan { font-size: 8px; }

  /* Back face */
  .band-top { position: absolute; left: 0; right: 0; top: 26px; height: 18px; }
  .band-bottom { position: absolute; left: 0; right: 0; top: 292px; height: 18px; }
  .back-panel {
    position: absolute; left: 0; right: 0; top: 44px; height: 248px;
  }
  .back-brand {
    position: absolute; left: 34px; top: 54px;
    display: flex; flex-direction: column; gap: 5px;
  }
  .back-brand .wordmark { font-size: 12px; letter-spacing: 0.16em; }
  .back-brand .wordmark-square { width: 8px; height: 8px; }
  .back-brand .slogan { font-size: 6px; padding-left: 16px; }
  .rule { position: absolute; height: 1px; background: var(--ink); }
  .rule-left { left: 34px; top: 108px; width: 190px; }
  .rule-right { right: 40px; top: 40px; width: 170px; }
  .holder {
    position: absolute; left: 250px; top: 44px;
    text-align: center;
  }
  .holder-name {
    font-family: "Oswald", sans-serif; font-weight: 400;
    font-size: 28px; letter-spacing: 0.02em; color: var(--ink);
    line-height: 1.1;
  }
  .holder-role {
    font-size: 10px; letter-spacing: 0.5em; margin-top: 6px;
  }
  .contacts {
    position: absolute; left: 60px; right: 34px; bottom: 28px;
    display: flex; justify-content: space-between; align-items: center;
    font-size: 10px; letter-spacing: 0.06em;
  }
  .contact { display: flex; align-items: center; gap: 6px; }
  .contact svg { width: 14px; height: 14px; fill: none; stroke: var(--plum); stroke-width: 1.5; }
</style>
</head>
<body>
<main class="sheet">

  <section class="card card-front">
    <div class="silk" role="img" aria-label="Draped pink satin fabric"></div>
    <div class="front-frame gold">
      <div class="front-panel satin">
        <div class="front-inset">
          <div class="wordmark"><span class="wordmark-square"></span>GOWNHAVEN</div>
          <div class="slogan">EVENING GOWNS ON LOAN</div>
        </div>
      </div>
    </div>
  </section>

  <section class="card card-back">
    <div class="silk" role="img" aria-label="Draped pink satin fabric"></div>
    <div class="band-top gold"></div>
    <div class="back-panel satin">
      <div class="back-brand">
        <div class="wordmark"><span class="wordmark-square"></span>GOWNHAVEN</div>
        <div class="slogan">EVENING GOWNS ON LOAN</div>
      </div>
      <span class="rule rule-left"></span>
      <span class="rule rule-right"></span>
      <div class="holder">
        <div class="holder-name">YOUR NAME HERE</div>
        <div class="holder-role">YOUR POSITION</div>
      </div>
      <div class="contacts">
        <span class="contact">
          <svg viewBox="0 0 16 16"><path d="M3 2h3l1.5 3.5-2 1.2a8 8 0 0 0 3.8 3.8l1.2-2L14 10v3a1 1 0 0 1-1 1A11 11 0 0 1 2 3a1 1 0 0 1 1-1z"/></svg>
          (123) 456 7890
        </span>
        <span class="contact">
          <svg viewBox="0 0 16 16"><path d="M8 15s5-5 5-9a5 5 0 0 0-10 0c0 4 5 9 5 9z"/><circle cx="8" cy="6" r="1.8"/></svg>
          123 N. STREET, CITY, STATE 12345
        </span>
        <span class="contact">
          <svg viewBox="0 0 16 16"><rect x="1.5" y="3.5" width="13" height="9"/><path d="M1.5 3.5 8 9l6.5-5.5"/></svg>
          NAME@COMPANY.COM
        </span>
      </div>
    </div>
    <div class="band-bottom gold"></div>
  </section>

</main>
</body>
</html>
```